New Business Cards for 3 companies - print and digital Needed FAST!

We have rebranded our company into three separate companies.
We need new business cards for 8 employees, three of whom need a business card for each company - total of 12 cards.
Pelmary is our property development company.
Velta Brokerage & Management handles property management and real estate transactions.
Oakwren Design Build is our construction company.
Business cards MUST be able to be both printed and function as digital business cards.
No black backgrounds.
Front should be each employee's information and include the logo from their primary company.
Back should include all three logos.
Please see the uploaded spreadsheet for all the information you need for each card. Also uploaded the .png files for each logo as well as the style guide for each logo.

Contact Information for Business Card

See uploaded spreadsheet for information

Font styles to use
Sans Serif
Other font styles liked:
• match style guide if possible

Requirements
Should not have
• No dark backgrounds on the front (on the back OK.) No pictures of employees. Thanks!

```html
<!DOCTYPE html>
<html lang="en">
<head>
<meta charset="utf-8">
<title>Pelmary Business Card – Front and Back</title>
<link rel="stylesheet" href="https://fonts.googleapis.com/css2?family=Montserrat:wght@400;500;600;700&display=swap">
<style>
  :root {
    --green: #7cc242;
    --ink: #3c3c3c;
    --muted: #555555;
    --orange: #f15a22;
    --blue: #1f74bf;
    --card: #ffffff;
    --backdrop: #e6e7e9;
  }
  * { box-sizing: border-box; margin: 0; padding: 0; }
  html, body {
    width: 1200px; height: 900px; overflow: hidden;
    background: var(--backdrop);
    font-family: "Montserrat", Arial, sans-serif;
    color: var(--ink);
  }
  .sheet { position: relative; width: 1200px; height: 900px; }
  .card {
    position: absolute; left: 250px; width: 700px; height: 400px;
    background: var(--card); border-radius: 22px;
    box-shadow: 0 6px 20px rgba(0,0,0,0.12);
  }
  .card--front { top: 30px; }
  .card--back { top: 470px; }

  /* wordmark lockup */
  .brand { position: absolute; display: flex; align-items: center; gap: 14px; }
  .brand__square { width: 58px; height: 58px; background: var(--green); }
  .brand__name { font-weight: 600; font-size: 44px; letter-spacing: 1px; color: var(--ink); line-height: 1; }
  .brand__tagline {
    position: absolute; font-size: 12px; letter-spacing: 2px; text-transform: uppercase;
    color: var(--ink); font-weight: 500;
  }

  /* front */
  .front__brand { left: 48px; top: 74px; }
  .front__tagline { left: 120px; top: 146px; padding-bottom: 8px; width: 230px; border-bottom: 1.5px solid var(--green); }
  .front__divider { position: absolute; left: 390px; top: 60px; width: 1.5px; height: 240px; background: var(--green); }
  .contact { position: absolute; left: 412px; top: 66px; font-size: 14px; line-height: 1.5; color: var(--muted); }
  .contact__name { font-size: 22px; font-weight: 700; color: var(--green); line-height: 1.2; }
  .contact__title { font-size: 15px; margin-bottom: 10px; }
  .contact__address { margin-bottom: 12px; }
  .contact__row { display: flex; align-items: center; gap: 8px; }
  .contact__row svg { width: 13px; height: 13px; flex: none; }
  .licenses {
    position: absolute; left: 48px; bottom: 42px; font-size: 14px; color: var(--muted);
    display: flex; align-items: center; gap: 12px;
  }
  .licenses__dot { width: 6px; height: 6px; background: var(--green); }
  .licenses b { font-weight: 600; }

  /* back */
  .back__pelmary { left: 56px; top: 48px; }
  .back__pelmary .brand__name { font-size: 34px; }
  .back__pelmary .brand__square { width: 46px; height: 46px; }
  .back__tagline { left: 116px; top: 102px; font-size: 10px; }
  .back__velta { left: 150px; top: 170px; flex-direction: column; align-items: flex-start; gap: 6px; }
  .back__velta .brand__name { color: var(--orange); font-size: 44px; }
  .back__oakwren { right: 56px; bottom: 52px; flex-direction: column; align-items: flex-end; gap: 6px; }
  .back__oakwren .brand__name { color: var(--blue); font-size: 44px; }
  .brand__sub { font-size: 12px; letter-spacing: 3px; text-transform: uppercase; color: var(--ink); font-weight: 500; }
</style>
</head>
<body>
<main class="sheet">

  <section class="card card--front" aria-label="Card front">
    <div class="brand front__brand">
      <span class="brand__square"></span>
      <span class="brand__name">Pelmary</span>
    </div>
    <p class="brand__tagline front__tagline">Invest. Build. Manage.</p>

    <div class="front__divider"></div>

    <div class="contact">
      <p class="contact__name">Daniel Ashford</p>
      <p class="contact__title">CEO/Owner</p>
      <p class="contact__address">418 N. Linden Ave., Ste 3B,<br>Maplewood IL 60499</p>
      <p class="contact__row">
        <svg viewBox="0 0 16 16"><rect x="4" y="1" width="8" height="14" rx="1.5" fill="none" stroke="#7cc242" stroke-width="1.6"/></svg>
        555-014-2287
      </p>
      <p class="contact__row">
        <svg viewBox="0 0 16 16"><path d="M3 1.5l3 .5 1 3.5-2 1.2a9 9 0 0 0 4.3 4.3l1.2-2 3.5 1 .5 3c-.2.7-1 1.2-2 1A12.5 12.5 0 0 1 1.5 3.5c-.2-1 .3-1.8 1.5-2z" fill="#7cc242"/></svg>
        555-016-4410 x101
      </p>
      <p class="contact__row">
        <svg viewBox="0 0 16 16"><rect x="1" y="3" width="14" height="10" fill="#7cc242"/><path d="M1 3l7 5.5L15 3" fill="none" stroke="#fff" stroke-width="1.3"/></svg>
        dashford@pelmary.com
      </p>
      <p class="contact__row">
        <svg viewBox="0 0 16 16"><circle cx="8" cy="8" r="7" fill="#7cc242"/><path d="M1 8h14M8 1c-3 3-3 11 0 14M8 1c3 3 3 11 0 14" fill="none" stroke="#fff" stroke-width="1"/></svg>
        www.pelmary.com
      </p>
    </div>

    <p class="licenses">
      <span><b>IL RE Lic#:</b> 471.093318 Chicago</span>
      <span class="licenses__dot"></span>
      <span><b>GC Lic #:</b> TGC052918</span>
    </p>
  </section>

  <section class="card card--back" aria-label="Card back">
    <div class="brand back__pelmary">
      <span class="brand__square"></span>
      <span class="brand__name">Pelmary</span>
    </div>
    <p class="brand__tagline back__tagline">Invest. Build. Manage.</p>

    <div class="brand back__velta">
      <span class="brand__name">Velta</span>
      <span class="brand__sub">Brokerage | Management</span>
    </div>

    <div class="brand back__oakwren">
      <span class="brand__name">Oakwren</span>
      <span class="brand__sub">Design | Build</span>
    </div>
  </section>

</main>
</body>
</html>
```